Project Finance Brochure

We are a finance fund helping bring energy efficiency and clean energy projects into the world. We would like a professionally created back and front brochure. Please take our internally created piece and work your magic!

Target Market(s)

We are targeting building owners, hotel operators, manufacturing plant engineers.

Industry/Entity Type

Finance

Font styles to use
Sans Serif

Requirements
Must have
• Must be clear and easy to understand. Flow charts help.
Nice to have
• Colors, fonts.

```html
<!DOCTYPE html>
<html lang="en">
<head>
<meta charset="utf-8">
<title>Solvane capital — Clean Energy Acceleration Program</title>
<link rel="stylesheet" href="https://fonts.googleapis.com/css2?family=Mulish:wght@400&display=swap">
<style>
  :root {
    --paper: #ffffff;
    --ink-grey: #6b6c6f;
    --title-grey: #7a7b7e;
    --tile-violet: #8a90c4;
    --tile-blue: #5b8fc8;
    --tile-teal: #2a86bf;
    --tile-sky: #7fb2d6;
    --tile-deep: #2f5f9a;
  }
  * { margin: 0; padding: 0; box-sizing: border-box; }
  html, body {
    width: 848px;
    height: 1200px;
    overflow: hidden;
    background: var(--paper);
  }
  .brochure-cover {
    position: relative;
    width: 848px;
    height: 1200px;
    background: var(--paper);
    font-family: "Mulish", sans-serif;
    overflow: hidden;
  }
  .brand {
    position: absolute;
    left: 64px;
    top: 52px;
    color: var(--ink-grey);
    font-weight: 400;
    line-height: 1;
  }
  .brand-name {
    display: block;
    font-size: 92px;
    letter-spacing: -1px;
  }
  .brand-sub {
    display: block;
    font-size: 46px;
    margin-top: 4px;
  }
  .program-title {
    position: absolute;
    left: 52px;
    top: 268px;
    font-size: 27px;
    font-weight: 400;
    font-variant: small-caps;
    letter-spacing: 0.5px;
    color: var(--title-grey);
  }
  .cover-artwork {
    position: absolute;
    left: 0;
    top: 0;
    width: 848px;
    height: 1200px;
  }
</style>
</head>
<body>
  <main class="brochure-cover">
    <div class="brand">
      <span class="brand-name">Solvane</span>
      <span class="brand-sub">capital</span>
    </div>

    <h1 class="program-title">Clean Energy Acceleration Program</h1>

    <svg class="cover-artwork" viewBox="0 0 848 1200" role="img"
         aria-label="Decorative field of overlapping translucent blue and violet hexagons">
      <defs>
        <linearGradient id="tile-field" x1="0" y1="0" x2="0.6" y2="1">
          <stop offset="0" stop-color="var(--tile-violet)"/>
          <stop offset="0.35" stop-color="var(--tile-blue)"/>
          <stop offset="0.6" stop-color="var(--tile-teal)"/>
          <stop offset="0.8" stop-color="var(--tile-deep)"/>
          <stop offset="1" stop-color="var(--tile-sky)"/>
        </linearGradient>
      </defs>
      <polygon fill="url(#tile-field)"
        points="0,742 82,776 143,662 192,552 313,463 447,523 570,430 703,490 820,396 848,408 848,1200 0,1200"/>
    </svg>
  </main>
</body>
</html>
```